Hardcore nerd needs to stand out in a sea of dull Defence business cards

Wombeck Dynamics is a new Australian consulting engineering company that turns research and theory into practical systems. No evangelistic fluff, just mathematics and physics into electronic and optical circuits for consumer products, scientific research or Defence applications.

We already have a recognised logo (provided) which is often dark blue/black on a light background but we're open to other combinations. (Us engineers tend to have limited aesthetic imagination :)

Some of our recent products have included:
* Instrumentation for electrical testing,
* Radar jammers,
* GPS antenna design,
* Satellite tracking systems,
* High power lasers

We're open to both single and double-sided designs - happy to be convinced either way.

P.S. Another group is working on the web page, so - alas - our web site is currently of no use for images/ideas...

Target Market(s)

Engineering managers,
Scientists

Contact Information for Business Card

Dr Martin Folsey
R&D Engineer

martin@wombeckdynamics.com.au
0427 563 201

PO Box XXX (to be confirmed)
Brindlow ACT 2914
Australia

Font styles to use
Serif
Sans Serif

Colors

Designer to choose colors to be used in the design.

Requirements
Must have
• My contact details!
• I've had many (great) "bold and plain" designs submitted already, so feel free to be artistically creative :)
• Happy to take advice re fonts/colours/printability etc.
Nice to have
• I'm not sure if "lists" are more at home on a CV than a business card, but representative services include:
• Applied electromagnetics
• RF and high speed electronics
• Signal and image processing
• Electro-optical and laser systems
• Concept-to-prototype design services
• If you're considering double sided cards, then often measuring/alignment grids/rulers feature on the back of similar cards.
• e.g. https://www.kelvorin.com/newgrouppage9.cfm?objectgroup_id=4183
• https://www.kelvorin.com/newgrouppage9.cfm?objectgroup_ID=4185
• ..or even a "Smith chart" (google will return lots)
• Generic images to represent a capability might work - googling images associated with keyword for each of these areas might help:
• - "passive radar", "phased array", "fdtd", "vircator"
• RF and high speed electronic design
• - "smith chart", "microstrip circuits", "dimensioned drawing", "electronic schematic"
• - "dft", "iir filter"
• - "optical cavity". "laser energy level diagram"
• Background/watermarked images outlines/wireframes/schematics would probably look OK.
Should not have
• If a list of projects/services is provided, it is important not to make the client feel that this is "all" the company can do. Engineering design is a creative discipline (like graphics :)
• Please, no stock "military" snaps like planes, missiles, etc!

```html
<!DOCTYPE html>
<html lang="en">
<head>
<meta charset="utf-8">
<title>Wombeck Dynamics — Business Card</title>
<link href="https://fonts.googleapis.com/css2?family=Lato:wght@400;700&display=swap" rel="stylesheet">
<style>
  :root {
    --stage: #5a5a5a;
    --stage-edge: #3a3a3a;
    --card-dark: #4a4a4a;
    --card-light: #ffffff;
    --ink-dark: #3b3b3b;
    --ink-mid: #5c5c5c;
    --ink-light: #ffffff;
    --rule: #3b3b3b;
    --faint: #f0f0f0;
  }
  * { box-sizing: border-box; margin: 0; padding: 0; }
  html, body { width: 1200px; height: 675px; overflow: hidden; }
  body {
    background: radial-gradient(ellipse at 50% 40%, var(--stage) 0%, var(--stage-edge) 100%);
    font-family: "Lato", sans-serif;
    position: relative;
  }
  .card {
    position: absolute;
    width: 520px;
    height: 297px;
    overflow: hidden;
    box-shadow: 0 6px 18px rgba(0,0,0,0.35);
  }
  .card--back { left: 70px; top: 60px; background: var(--card-dark); color: var(--ink-light); }
  .card--front { left: 610px; top: 318px; background: var(--card-light); color: var(--ink-dark); }

  .brand { position: absolute; display: flex; align-items: center; gap: 10px; z-index: 2; }
  .brand__mark { width: 40px; height: 40px; border-radius: 50%; flex: none; }
  .brand__name { font-weight: 700; letter-spacing: 1px; text-transform: uppercase; line-height: 1; white-space: nowrap; }

  .card--back .brand { left: 34px; top: 88px; }
  .card--back .brand__mark { background: var(--ink-light); width: 36px; height: 36px; }
  .card--back .brand__name { font-size: 18px; }

  .services { position: absolute; left: 50px; top: 168px; z-index: 2; }
  .services__title { font-size: 17px; font-weight: 700; margin-bottom: 6px; }
  .services__list { list-style: none; font-size: 13px; line-height: 19px; }
  .services__list li { display: flex; align-items: center; gap: 6px; padding-left: 8px; white-space: nowrap; }
  .services__list svg { width: 10px; height: 10px; flex: none; }

  .chart-area {
    position: absolute; right: 16px; top: 18px; width: 206px; height: 206px; border-radius: 50%;
    background: radial-gradient(circle at 50% 50%, #6a6a6a 0%, #565656 70%, #4f4f4f 100%);
    z-index: 1;
  }

  .card--front .decor {
    position: absolute; right: -60px; top: -70px; width: 260px; height: 260px; border-radius: 50%;
    background: var(--faint);
  }
  .card--front .brand { left: 34px; top: 72px; }
  .card--front .brand__mark { background: var(--ink-dark); }
  .card--front .brand__name { font-size: 21px; }

  .rule { position: absolute; height: 1px; background: var(--rule); }
  .rule--top { left: 200px; right: 30px; top: 128px; }
  .rule--mid { left: 40px; width: 170px; top: 212px; }

  .person { position: absolute; left: 40px; top: 164px; }
  .person__name { font-weight: 700; font-size: 19px; }
  .person__role { font-size: 12px; color: var(--ink-mid); margin-top: 2px; }

  .contact { position: absolute; left: 40px; top: 222px; list-style: none; font-size: 12px; line-height: 18px; color: var(--ink-mid); }
  .contact li { display: flex; align-items: center; gap: 6px; }
  .contact svg { width: 10px; height: 10px; flex: none; fill: var(--ink-dark); }

  .address { position: absolute; right: 30px; top: 140px; text-align: right; font-size: 12px; line-height: 16px; color: var(--ink-mid); }
</style>
</head>
<body>

<section class="card card--back" aria-label="Card back">
  <div class="chart-area" role="img" aria-label="Smith chart line drawing in white on grey"></div>
  <div class="brand">
    <span class="brand__mark"></span>
    <span class="brand__name">Wombeck Dynamics</span>
  </div>
  <div class="services">
    <h2 class="services__title">Our Services:</h2>
    <ul class="services__list">
      <li><svg viewBox="0 0 10 10"><path d="M1 5 L4 8 L9 1" stroke="#fff" stroke-width="2" fill="none"/></svg>Applied electromagnetics</li>
      <li><svg viewBox="0 0 10 10"><path d="M1 5 L4 8 L9 1" stroke="#fff" stroke-width="2" fill="none"/></svg>RF and high speed electronics</li>
      <li><svg viewBox="0 0 10 10"><path d="M1 5 L4 8 L9 1" stroke="#fff" stroke-width="2" fill="none"/></svg>Signal and image processing</li>
      <li><svg viewBox="0 0 10 10"><path d="M1 5 L4 8 L9 1" stroke="#fff" stroke-width="2" fill="none"/></svg>Electro-optical and laser systems</li>
      <li><svg viewBox="0 0 10 10"><path d="M1 5 L4 8 L9 1" stroke="#fff" stroke-width="2" fill="none"/></svg>Concept-to-prototype design services</li>
    </ul>
  </div>
</section>

<section class="card card--front" aria-label="Card front">
  <div class="decor" aria-hidden="true"></div>
  <div class="brand">
    <span class="brand__mark"></span>
    <span class="brand__name">Wombeck Dynamics</span>
  </div>
  <div class="rule rule--top"></div>
  <div class="address">PO Box XXX (to be confirmed)<br>Brindlow ACT 2914, Australia</div>
  <div class="person">
    <p class="person__name">Dr Martin Folsey</p>
    <p class="person__role">R&amp;D Engineer</p>
  </div>
  <div class="rule rule--mid"></div>
  <ul class="contact">
    <li><svg viewBox="0 0 10 10"><path d="M2 0 L4 2.5 L3 4 Q4.5 6 6 7 L7.5 6 L10 8 L8.5 10 Q3 9 0 2 Z"/></svg>0427 563 201</li>
    <li><svg viewBox="0 0 10 10"><path d="M0 2 H10 V8 H0 Z M0 2 L5 6 L10 2" stroke="#3b3b3b" stroke-width="1" fill="none"/></svg>martin@wombeckdynamics.com.au</li>
    <li><svg viewBox="0 0 10 10"><circle cx="5" cy="5" r="4.3" fill="none" stroke="#3b3b3b" stroke-width="1"/><ellipse cx="5" cy="5" rx="2" ry="4.3" fill="none" stroke="#3b3b3b" stroke-width="0.8"/><path d="M0.7 5 H9.3" stroke="#3b3b3b" stroke-width="0.8"/></svg>wombeckdynamics.com.au</li>
  </ul>
</section>

</body>
</html>
```